Corrindale Planners, LLC Stationary

Corrindale Planners, LLC is a new financial planning and consulting company. We are looking for designs on business cards, letterhead, envelopes, and anything else that would be useful. Our preference for business card design is two sided. We are looking for a professional and clean look with incorporating the logo and patriotic feel. Thank you to all who participate and good luck!

```html
<!DOCTYPE html>
<html lang="en">
<head>
<meta charset="utf-8">
<title>Corrindale Planners, LLC – Business Card</title>
<link rel="stylesheet" href="https://fonts.googleapis.com/css2?family=Arimo:wght@400;700&display=swap">
<style>
  :root {
    --navy: #1c3f6e;
    --navy-deep: #13305a;
    --red: #d3262c;
    --grey: #555c66;
    --rule: #b9bec6;
    --paper: #ffffff;
    --stage: #e9ebee;
  }
  * { box-sizing: border-box; margin: 0; padding: 0; }
  html, body { width: 1200px; height: 950px; overflow: hidden; }
  body {
    background: var(--stage);
    font-family: "Arimo", Arial, sans-serif;
    position: relative;
  }
  .card {
    position: absolute;
    left: 250px;
    width: 700px;
    height: 400px;
    overflow: hidden;
    box-shadow: 0 6px 20px rgba(0,0,0,.18);
  }
  /* ---------- back side ---------- */
  .card-back {
    top: 50px;
    background: linear-gradient(135deg, #244c80 0%, var(--navy) 50%, var(--navy-deep) 100%);
    color: #fff;
    display: flex;
    flex-direction: column;
    align-items: center;
    justify-content: center;
  }
  .card-back .company-name {
    font-size: 40px;
    font-weight: 700;
    color: #fff;
  }
  .card-back .service-line {
    margin-top: 10px;
    font-size: 15px;
    color: #dfe6f0;
  }
  .card-back .web {
    margin-top: 28px;
    font-size: 20px;
    letter-spacing: 2px;
  }
  /* ---------- front side ---------- */
  .card-front {
    top: 500px;
    background: var(--paper);
  }
  .company {
    position: absolute;
    top: 72px;
    left: 0;
    right: 0;
    display: flex;
    flex-direction: column;
    align-items: center;
  }
  .company-row { display: flex; align-items: center; gap: 14px; }
  .company-square { width: 20px; height: 20px; background: var(--red); }
  .company .company-name {
    font-size: 34px;
    font-weight: 700;
    color: var(--navy);
  }
  .company .service-line {
    margin-top: 8px;
    font-size: 14px;
    color: var(--grey);
  }
  .details {
    position: absolute;
    top: 185px;
    left: 0;
    right: 0;
    display: flex;
    justify-content: center;
  }
  .person {
    text-align: right;
    padding-right: 24px;
    border-right: 1px solid var(--rule);
  }
  .person-name { font-size: 22px; font-weight: 700; color: var(--navy); }
  .person-title { font-size: 17px; font-weight: 700; color: var(--red); margin-bottom: 8px; }
  .address { font-size: 17px; line-height: 1.4; color: var(--grey); }
  .contacts { list-style: none; padding-left: 24px; padding-top: 12px; }
  .contacts li {
    display: flex; align-items: center; gap: 10px;
    font-size: 17px; line-height: 1.45; color: var(--grey);
  }
  .contacts svg { width: 16px; height: 16px; fill: var(--navy); flex: none; }
  .footer-rule {
    position: absolute;
    left: 0; right: 0; bottom: 38px;
    height: 1px;
    background: var(--red);
  }
  .footer-band {
    position: absolute;
    left: 0; right: 0; bottom: 0;
    height: 34px;
    background: var(--navy);
    border-top: 3px solid var(--red);
  }
</style>
</head>
<body>

<section class="card card-back" aria-label="Business card, back">
  <div class="company-name">Corrindale Planners, LLC</div>
  <div class="service-line">Financial Planning and Consulting</div>
  <div class="web">www.corrindale.com</div>
</section>

<section class="card card-front" aria-label="Business card, front">
  <div class="company">
    <div class="company-row">
      <span class="company-square"></span>
      <span class="company-name">Corrindale Planners, LLC</span>
    </div>
    <div class="service-line">Financial Planning and Consulting</div>
  </div>

  <div class="details">
    <div class="person">
      <div class="person-name">Marcus Hale</div>
      <div class="person-title">President</div>
      <div class="address">2417 Linden Crest Road<br>Ashbury Falls, NY 11502</div>
    </div>
    <ul class="contacts">
      <li><svg viewBox="0 0 16 16"><path d="M3 1h3l1.5 4-2 1.2a9 9 0 0 0 4.3 4.3L11 8.5l4 1.5v3a2 2 0 0 1-2 2A12 12 0 0 1 1 3a2 2 0 0 1 2-2z"/></svg>555 0187 4412</li>
      <li><svg viewBox="0 0 16 16"><path d="M4 1h7l1 1v4H4zM2 6h12a1 1 0 0 1 1 1v6H1V7a1 1 0 0 1 1-1zm2 4v5h8v-5z"/></svg>555 0163 9078</li>
      <li><svg viewBox="0 0 16 16"><path d="M1 3h14v1L8 9 1 4zM1 6l7 5 7-5v7H1z"/></svg>marcus@corrindale.com</li>
      <li><svg viewBox="0 0 16 16"><circle cx="8" cy="8" r="7"/><path d="M1 8h14M8 1c-3 3-3 11 0 14M8 1c3 3 3 11 0 14" stroke="#fff" stroke-width="1" fill="none"/></svg>www.corrindale.com</li>
    </ul>
  </div>

  <div class="footer-rule"></div>
  <div class="footer-band"></div>
</section>

</body>
</html>
```